International MultiIndustry Team Coaching Site

Hello Designers,
We need a redesign of the pages attached.
The design must be engaging and modern, with a focus on the user experience, particularly for the "observations" page. Because this is the main page of the website. It is to be used on a 10'' tablet or desktop, to record observations on the fly, so it must be intuitive and efficient.
The positioning of the metrics and observations and etc, are just a reference. you can switch it up if you feel there is a better way (PLEASE DO ;) ).

There are many categories (color coded with borders in the example hpt_6_observations.jpg) and observation metrics within each category. This is the Key page, because it is the One with the most interactions.

The user should know when it has selected a category (there should be some visual hint) and the different metric widgets should be accounted for.
There are 3: The time widget at the end, numerical widgets (recording more or less numbers), and boolean ones (selected or not).

For the numerical widgets, we show plus and minus characters, but you can change this, being creative, keeping in mind that it must work well on a mobile device and desktop, and must be intuitive and quick.

Set your creativity free with the login screen , home screen, categories secret, events screen, journaling and observations screen .

We would like the site/mobile version to have a very modern look. Something that would be found in very popular and user friendly apps.

***** The events, journaling, category and home screens are getting 2 much attention , please focus also on the observations screen *******
Imagine you are a psychologist tasked with observing the behaviour of teenagers during group work. And you have a tablet on which to record what you observe. Now imagine you need to observe during 3 classes: Biology, Math, Physics (these are events). For each class (event) you will have to record observations in 3 categories: Social Interaction, Leadership, Communication (these are categories).
Example of the metrics (these are observations) for Leadership:
" the teenager direct other colleagues" (boolean widget),
"the teenager speaks more than everyone else" (boolean widget)
"the teenager interrupts colleagues speaking" (number widget)
"the work took hh:mm" (time widget)

The observations screen can have any shape and form you think of. It doesn't need to be that single column with yes and nos, or that double column with the squared cards.
thank you.

Hope that was useful intel :)
Available for any questions you might have.
Good luck :)

Enterprise teams

5+ page

Sans Serif

• Modern design

```html
<!DOCTYPE html>
<html lang="en">
<head>
<meta charset="UTF-8">
<title>Crewline – Home</title>
<link href="https://fonts.googleapis.com/css2?family=Roboto+Slab:wght@500;600&family=Roboto:wght@400;500&display=swap" rel="stylesheet">
<style>
  :root {
    --header-bg: #e9e9e9;
    --page-bg: #ffffff;
    --card-blue: #bcd6f2;
    --card-grey: #dcdcdc;
    --accent-blue: #4f87c8;
    --accent-pink: #c44f7a;
    --accent-purple: #5b4a97;
    --ink: #1c1c1c;
    --ink-soft: #3b3b3b;
    --white: #ffffff;
  }
  * { box-sizing: border-box; margin: 0; padding: 0; }
  html, body { width: 1200px; height: 675px; overflow: hidden; }
  body {
    font-family: "Roboto Slab", Georgia, serif;
    color: var(--ink);
    background: linear-gradient(120deg, var(--page-bg) 45%, #ececec 80%, #e2e2e2 100%);
    position: relative;
  }
  .app-header {
    position: absolute; left: 0; top: 0; width: 1200px; height: 80px;
    background: var(--header-bg);
    box-shadow: 0 2px 3px rgba(0,0,0,0.12);
  }
  .brand {
    position: absolute; left: 60px; top: 26px;
    display: flex; align-items: center; gap: 10px;
    font-family: "Roboto Slab", Georgia, serif; font-weight: 600;
    font-size: 22px; color: var(--accent-blue);
  }
  .brand-dot { width: 20px; height: 20px; border-radius: 50%; background: var(--accent-blue); }
  .user-pill {
    position: absolute; left: 942px; top: 20px; width: 233px; height: 40px;
    border-radius: 20px; background: var(--card-blue);
    display: flex; align-items: center; padding-left: 4px;
    font-family: "Roboto", Arial, sans-serif;
  }
  .user-avatar { width: 34px; height: 34px; border-radius: 50%; background: linear-gradient(160deg, #8fb3d6, #e8eef4); }
  .user-text { margin-left: 9px; line-height: 1.15; }
  .user-name { font-size: 14px; font-weight: 500; }
  .user-role { font-size: 12px; color: var(--ink-soft); }
  .user-caret { position: absolute; right: 46px; top: 16px; }

  .card {
    position: absolute; border-radius: 10px;
    box-shadow: 2px 3px 5px rgba(0,0,0,0.2);
  }
  .card--blue { background: var(--card-blue); }
  .card--grey { background: var(--card-grey); }
  .card--tall { top: 110px; width: 230px; height: 230px; }
  .card--wide { top: 440px; width: 324px; height: 110px; }

  .thumb {
    position: absolute; width: 80px; height: 80px; border-radius: 50%;
    border: 2px solid var(--accent-blue);
    background: linear-gradient(180deg, #3d78c0 0%, #9dc3e8 50%, #e9eef4 75%, #c6d3e0 100%);
  }
  .add-circle {
    position: absolute; width: 80px; height: 80px; border-radius: 50%;
    border: 2px solid var(--accent-blue); background: rgba(255,255,255,0.15);
  }
  .add-circle svg { position: absolute; left: 20px; top: 20px; }

  .card-title { position: absolute; font-weight: 600; font-size: 22px; white-space: nowrap; }
  .btn {
    position: absolute; border-radius: 3px; color: var(--white);
    font-family: "Roboto Slab", Georgia, serif; font-size: 20px; font-weight: 500;
    display: flex; align-items: center; justify-content: center;
  }
  .btn--blue { background: var(--accent-blue); }
  .btn--pink { background: var(--accent-pink); }
  .btn--small { font-size: 17px; }

  .dot { position: absolute; width: 28px; height: 28px; border-radius: 50%; top: 128px; }

  .section-title { position: absolute; left: 60px; top: 393px; font-size: 22px; font-weight: 600; }
  .card-actions { position: absolute; left: 144px; top: 80px; }
</style>
</head>
<body>
  <header class="app-header">
    <div class="brand"><span class="brand-dot"></span>Crewline</div>
    <div class="user-pill">
      <div class="user-avatar" role="img" aria-label="Profile photo of the signed-in officer"></div>
      <div class="user-text">
        <div class="user-name">Dana Pierce</div>
        <div class="user-role">Fly Officer</div>
      </div>
      <svg class="user-caret" width="12" height="8" viewBox="0 0 12 8"><path d="M1 1l5 5 5-5" stroke="#111" stroke-width="2.2" fill="none"/></svg>
    </div>
  </header>

  <section class="card card--blue card--tall" style="left:60px">
    <div class="thumb" style="left:75px;top:16px" role="img" aria-label="Airliner climbing above clouds"></div>
    <div class="card-title" style="left:0;width:230px;text-align:center;top:108px">My Jounaling</div>
    <div class="btn btn--blue" style="left:36px;top:150px;width:158px;height:36px">View</div>
    <div class="btn btn--pink" style="left:36px;top:193px;width:158px;height:36px">Delete</div>
  </section>

  <section class="card card--grey card--tall" style="left:326px">
    <div class="add-circle" style="left:75px;top:16px">
      <svg width="40" height="40" viewBox="0 0 40 40"><path d="M20 3v34M3 20h34" stroke="#4f87c8" stroke-width="7" stroke-linecap="round"/></svg>
    </div>
    <span class="dot" style="left:44px;background:var(--accent-blue)"></span>
    <span class="dot" style="left:99px;background:var(--accent-pink)"></span>
    <span class="dot" style="left:153px;background:var(--accent-purple)"></span>
    <div class="btn btn--blue btn--small" style="left:36px;top:168px;width:158px;height:36px">New Narrative</div>
  </section>

  <h2 class="section-title">All Teams</h2>

  <section class="card card--blue card--wide" style="left:60px">
    <div class="thumb" style="left:14px;top:15px" role="img" aria-label="Airliner climbing above clouds"></div>
    <div class="card-title" style="left:143px;top:28px">Grean Team</div>
    <svg class="card-actions" width="140" height="22" viewBox="0 0 140 22">
      <path d="M2 1h10l5 5v15H2z" fill="#3366b3"/><path d="M5 17l4-8 3 8M6 14h5" stroke="#fff" stroke-width="1.3" fill="none"/>
      <g fill="#3366b3"><rect x="42" y="19" width="21" height="2"/><rect x="42" y="6" width="2" height="15"/><rect x="47" y="11" width="2.5" height="7"/><rect x="51" y="7" width="2.5" height="11"/><rect x="55" y="9" width="2.5" height="9"/><rect x="59" y="5" width="2.5" height="13"/></g>
      <path d="M118 4h16v2h-16zM123 1h6v3h-6zM119 7h14l-1 15h-12z" fill="#c44f7a"/>
    </svg>
  </section>

  <section class="card card--blue card--wide" style="left:425px">
    <div class="thumb" style="left:14px;top:15px" role="img" aria-label="Airliner climbing above clouds"></div>
    <div class="card-title" style="left:143px;top:28px">Hard Count</div>
    <svg class="card-actions" width="140" height="22" viewBox="0 0 140 22">
      <path d="M2 1h10l5 5v15H2z" fill="#3366b3"/><path d="M5 17l4-8 3 8M6 14h5" stroke="#fff" stroke-width="1.3" fill="none"/>
      <g fill="#3366b3"><rect x="42" y="19" width="21" height="2"/><rect x="42" y="6" width="2" height="15"/><rect x="47" y="11" width="2.5" height="7"/><rect x="51" y="7" width="2.5" height="11"/><rect x="55" y="9" width="2.5" height="9"/><rect x="59" y="5" width="2.5" height="13"/></g>
      <path d="M118 4h16v2h-16zM123 1h6v3h-6zM119 7h14l-1 15h-12z" fill="#c44f7a"/>
    </svg>
  </section>

  <section class="card card--grey card--wide" style="left:790px">
    <div class="add-circle" style="left:18px;top:15px">
      <svg width="40" height="40" viewBox="0 0 40 40"><path d="M20 3v34M3 20h34" stroke="#4f87c8" stroke-width="7" stroke-linecap="round"/></svg>
    </div>
    <div class="btn btn--blue btn--small" style="left:139px;top:38px;width:158px;height:36px">New Narrative</div>
  </section>
</body>
</html>
```